Retail Appliance Store Chain needs NEW business Card

Name of my company is Brennan's Appliances brennansappliances.example is our website. . We are a 2 location brick and mortar, and online store selling premium, luxury, and normal household appliances, such as ovens, stoves, cooktops, dishwashers, refrigerators, washers and dryers, grills, air conditioners etc. The focus is on large kitchen appliances and laundry appliances.
Please visit http://brennansappliances.example to get a feel for the business and branding.
I have attached the Brennan's Appliances logo (i do not have eps or psd or ai). And I have also attached our current business cards that we use. We have two versions. A double sided version for managers, and a one side version for regular employees.
Please submit BOTH one sided and two sided designs if possible.
Please keep consistent with the Brennan's Appliances logo, colors, etc.
I would prefer no rounded corners on the business card designs for printing costs.
Information on the cards (in no particular order):
Name - Employee Name
Business name - Brennan's Appliances
website - brennansappliances.example
Email - Employee Email
2 Phone Numbers - store 1 address, store 2 address
2 Addresses - store 1 address, store 2 address

*do NOT need Fax #

Industry/Entity Type

Home Appliance

Contact Information for Business Card

Logo - Brennans Appliances Logo
Name - Employee Name
Email - Employee Email

Please no rounded corners. Standard US Business Card Size please.

Font styles to use
Serif
Sans Serif

Requirements
Must have
• colors and design that somewhat match the feel of current logo and website
Should not have
• No rounded corners.
No non-traditional business card size. US Standard Business Card Size only

```html
<!DOCTYPE html>
<html lang="en">
<head>
<meta charset="utf-8">
<title>Brennan's Appliances – Business Cards</title>
<link href="https://fonts.googleapis.com/css2?family=Open+Sans:wght@400;600;700&display=swap" rel="stylesheet">
<style>
  :root {
    --backdrop: #e4e4e4;
    --card: #2b2b2b;
    --brand-blue: #1e7fe6;
    --emboss: #3a3a3a;
    --white: #f2f2f2;
  }
  html, body {
    margin: 0;
    width: 1200px;
    height: 801px;
    overflow: hidden;
    background: var(--backdrop);
    font-family: "Open Sans", Arial, sans-serif;
  }
  .sheet {
    width: 1200px;
    height: 801px;
    display: flex;
    align-items: center;
    justify-content: center;
    gap: 40px;
  }
  .card {
    position: relative;
    width: 540px;
    height: 309px;
    background: var(--card);
    border-bottom: 4px solid var(--brand-blue);
    border-left: 4px solid var(--brand-blue);
    box-sizing: border-box;
    overflow: hidden;
  }
  /* front */
  .front .wordmark {
    position: absolute;
    top: 38px;
    right: 36px;
    color: var(--brand-blue);
    font-weight: 700;
    font-size: 28px;
    letter-spacing: 0.5px;
  }
  .front .rule-top {
    position: absolute;
    left: 0;
    right: 0;
    top: 104px;
    height: 1px;
    background: var(--brand-blue);
  }
  .front .identity {
    position: absolute;
    left: 34px;
    top: 128px;
    color: var(--brand-blue);
    line-height: 1.25;
  }
  .identity .name { font-size: 21px; font-weight: 700; }
  .identity .role, .identity .branch { font-size: 13px; font-weight: 400; }
  .front .rule-short {
    position: absolute;
    left: 34px;
    top: 205px;
    width: 190px;
    height: 1px;
    background: var(--brand-blue);
  }
  .front .contacts {
    position: absolute;
    left: 34px;
    top: 214px;
    margin: 0;
    padding: 0;
    list-style: none;
    color: var(--brand-blue);
    font-size: 13px;
    line-height: 24px;
  }
  .contacts li { display: flex; align-items: center; gap: 10px; }
  .contacts svg { width: 12px; height: 12px; flex: none; }
  /* back */
  .back .emboss-mark {
    position: absolute;
    top: 70px;
    left: 0;
    right: 0;
    text-align: center;
    color: var(--emboss);
    font-weight: 700;
    font-size: 40px;
    letter-spacing: 1px;
  }
  .back .store {
    position: absolute;
    bottom: 22px;
    color: var(--white);
    font-size: 13px;
    line-height: 19px;
  }
  .store.primary { left: 30px; text-align: left; }
  .store.secondary { right: 30px; bottom: 110px; text-align: right; }
</style>
</head>
<body>
<main class="sheet">
  <section class="card front">
    <div class="wordmark">Brennan's Appliances</div>
    <div class="rule-top"></div>
    <div class="identity">
      <div class="name">Dana Whitfield</div>
      <div class="role">Bargain Basement Supervisor</div>
      <div class="branch">Ashford</div>
    </div>
    <div class="rule-short"></div>
    <ul class="contacts">
      <li>
        <svg viewBox="0 0 12 12" aria-hidden="true"><path d="M2.5 1h2l1 2.5-1.3 1a6 6 0 0 0 3.3 3.3l1-1.3L11 7.5v2A1.5 1.5 0 0 1 9.5 11 8.5 8.5 0 0 1 1 2.5 1.5 1.5 0 0 1 2.5 1z" fill="currentColor"/></svg>
        (860) 555-0142 ext.10
      </li>
      <li>
        <svg viewBox="0 0 12 12" aria-hidden="true"><rect x="1" y="2.5" width="10" height="7" fill="none" stroke="currentColor" stroke-width="1.2"/><path d="M1 2.5l5 4 5-4" fill="none" stroke="currentColor" stroke-width="1.2"/></svg>
        danaw@brennansappliances.example
      </li>
      <li>
        <svg viewBox="0 0 12 12" aria-hidden="true"><circle cx="6" cy="6" r="5" fill="none" stroke="currentColor" stroke-width="1.2"/><ellipse cx="6" cy="6" rx="2.2" ry="5" fill="none" stroke="currentColor" stroke-width="1"/><path d="M1 6h10" stroke="currentColor" stroke-width="1"/></svg>
        www.brennansappliances.example
      </li>
    </ul>
  </section>

  <section class="card back">
    <div class="emboss-mark">Brennan's Appliances</div>
    <address class="store secondary">
      14 Lantern Wharf Ave.<br>
      Harbor Point, CT 06391<br>
      (860) 555-0173<br>
      Fax (860) 555-0199
    </address>
    <address class="store primary">
      88 Quarry Hill Rd.<br>
      Ashford, CT 06278<br>
      (860) 555-0142<br>
      Fax (860) 555-0199
    </address>
  </section>
</main>
</body>
</html>
```